Calder Ridge Minerals

Looking for a cool, glossy business card...white with our logo on one side and then the a smaller version of the logo on the other side (top left hand corner) and then the name and position of the person next to it, and then the office address and email address on the bottom left hand corner and the phone numbers & email address on the bottom right hand corner. I have the logo already...can pass it on when you're ready.

```html
<!DOCTYPE html>
<html lang="en">
<head>
<meta charset="utf-8">
<title>Calder Ridge Minerals – Business Card</title>
<link href="https://fonts.googleapis.com/css2?family=Cinzel:wght@600&family=Montserrat:wght@400;500&display=swap" rel="stylesheet">
<style>
  :root {
    --page: #e4e5e7;
    --card: #ffffff;
    --band: #3a3c41;
    --ink: #2b2c30;
    --silver: #b9bcc2;
    --text-light: #e9eaec;
    --accent-blue: #2f45a8;
    --accent-red: #d4202c;
  }
  * { margin: 0; padding: 0; box-sizing: border-box; }
  html, body { width: 1200px; height: 965px; overflow: hidden; }
  body {
    background: var(--page);
    font-family: "Montserrat", sans-serif;
    position: relative;
  }
  .card {
    position: absolute;
    left: 232px;
    width: 736px;
    height: 420px;
    background: var(--card);
    box-shadow: 0 6px 18px rgba(0,0,0,.18);
    overflow: hidden;
  }
  .card--front { top: 40px; }
  .card--back { top: 505px; }

  .wordmark {
    position: absolute;
    font-family: "Cinzel", serif;
    font-weight: 600;
    color: var(--ink);
    white-space: nowrap;
  }
  .card--front .wordmark {
    left: 0; right: 0;
    top: 186px;
    text-align: center;
    font-size: 40px;
    letter-spacing: 1px;
  }
  .card--back .wordmark {
    left: 40px;
    top: 86px;
    font-size: 26px;
    letter-spacing: 1px;
  }

  .info-band {
    position: absolute;
    left: 0; right: 0; bottom: 0;
    height: 196px;
    background: var(--band);
    color: var(--text-light);
  }
  .accent-bar {
    position: absolute;
    left: 22px; top: 40px;
    width: 6px; height: 52px;
    background: var(--accent-blue);
  }
  .person {
    position: absolute;
    left: 42px; top: 34px;
  }
  .person__name {
    font-family: "Cinzel", serif;
    font-weight: 600;
    font-size: 30px;
    color: var(--silver);
    letter-spacing: 1px;
  }
  .person__role { font-size: 19px; margin-top: 2px; }

  .contact { list-style: none; position: absolute; font-size: 17px; }
  .contact li { display: flex; align-items: center; gap: 10px; height: 26px; white-space: nowrap; }
  .contact svg { width: 16px; height: 16px; fill: var(--accent-red); flex: none; }
  .contact--office { left: 42px; bottom: 26px; }
  .contact--direct { right: 30px; top: 40px; }
  .contact--direct li { justify-content: flex-end; }
</style>
</head>
<body>
  <section class="card card--front">
    <div class="wordmark">Calder Ridge Minerals</div>
  </section>

  <section class="card card--back">
    <div class="wordmark">Calder Ridge Minerals</div>
    <div class="info-band">
      <span class="accent-bar"></span>
      <div class="person">
        <div class="person__name">Warren Ashby</div>
        <div class="person__role">General Manager</div>
      </div>

      <ul class="contact contact--office">
        <li>
          <svg viewBox="0 0 16 16"><path d="M8 0a5.5 5.5 0 0 0-5.5 5.5C2.5 10 8 16 8 16s5.5-6 5.5-10.5A5.5 5.5 0 0 0 8 0zm0 8a2.5 2.5 0 1 1 0-5 2.5 2.5 0 0 1 0 5z"/></svg>
          1/3 first address, State, City ZIP
        </li>
        <li>
          <svg viewBox="0 0 16 16"><path d="M0 3h16v10H0z"/><path d="M0 3l8 6 8-6" fill="none" stroke="#3a3c41" stroke-width="1.4"/></svg>
          info@calderridgeminerals.com
        </li>
      </ul>

      <ul class="contact contact--direct">
        <li>+00 000 00 00 00
          <svg viewBox="0 0 16 16"><path d="M3.6 1l2.6 3-1.5 1.8c.9 2 2.5 3.6 4.5 4.5L11 8.8l3 2.6-1.6 2.8C6.4 14 2 9.6 1 3.6z"/></svg>
        </li>
        <li>+00 000 00 00 00
          <svg viewBox="0 0 16 16"><path d="M3.6 1l2.6 3-1.5 1.8c.9 2 2.5 3.6 4.5 4.5L11 8.8l3 2.6-1.6 2.8C6.4 14 2 9.6 1 3.6z"/></svg>
        </li>
        <li>info@warrenashby.com
          <svg viewBox="0 0 16 16"><path d="M0 3h16v10H0z"/><path d="M0 3l8 6 8-6" fill="none" stroke="#3a3c41" stroke-width="1.4"/></svg>
        </li>
      </ul>
    </div>
  </section>
</body>
</html>
```